Website created on Plorvix.com

I have a telecommunications company and i would like my website built on plorvix.com as this platform is easy for me to change in the future so the site needs to be made so i can change it when i need to. Also I have found Plorvix is very good for SEO setup
Examples of websites i like as they are clean and corporate www.dastrelo.com.au (on this site there are menus on the right hand side which changes the content on the same page I would like the also www.kovantirel.com.au
My company sells business phone systems we sell the following products
1. Hosted PBX (This is the main product/service we sell)
2. Tusrok products (Tusrok has a range of products Phone systems, Gateways and Software we sell all products)
3. Brondavi Phones (we sell the following Brondavi phones T46G, T42G, T41G, T28P, T26P, T22P, T20P, VP530, W52P, EXP39, EXP40
4. ZelPBX (www.quimbrel.com) we sell SoHo and all the U series plus the add on's
5. VoIP plans (this is a outbound phone service for business customer)
1. business starter ($0 month 0 call included .12c local calls .24c mobile calls
2. business saver ($25 month 250 local calls included .10c local calls .22c mobile calls
3. business super ($50 month 500 local calls included .09c local calls .20c mobile calls
4. business extreme ($100 month 1000 local calls included .08c local calls .18c mobile calls
home page
custom corporate banners for each product/service 1. Hosted PBX 2. VoIP Plans 3. Brondavi Phones 4. ZelPBX 5. Tusrok, Which will rotate every 4 seconds
next will be displaying the VoIP plans with links to the plans pages
next icons of 1. Hosted PBX, 2. Brondavi phones 3. ZelPBX 4. Tusrok with links to the right page within the site
next a section with a description and design of what the business can do you the customer, please give me some examples
Product pages for all products/services Hosted PBX, Brondavi, ZelPbx, Tusrok and VoIP plans
Please make a pages for Headsets and I will attached the brands later
The aim is to have a clean white corporate website that ranks very will in fenwora that I can manage in the future
Please do not copy my existing site
small to medium business
Telecommunications

```html
<!DOCTYPE html>
<html lang="en">
<head>
<meta charset="utf-8">
<title>Velmarrow Voice – Hosted PBX</title>
<link href="https://fonts.googleapis.com/css2?family=Arimo:wght@400;700&display=swap" rel="stylesheet">
<style>
:root{
  --navy:#0b2c4f;
  --navy-dark:#082341;
  --blue:#1a8fd6;
  --blue-mid:#137ac2;
  --blue-deep:#0c5c98;
  --text:#555;
  --muted:#777;
  --ghost:#dfe1e3;
  --white:#fff;
}
*{margin:0;padding:0;box-sizing:border-box}
html,body{width:798px;height:1200px;overflow:hidden}
body{font-family:"Arimo",Arial,sans-serif;color:var(--text);background:var(--white);position:relative}

/* top bar */
.topbar{position:absolute;top:0;left:0;width:798px;height:24px;background:var(--navy)}
.topbar .call{position:absolute;left:83px;top:7px;font-size:8px;color:var(--blue);display:flex;align-items:center;gap:5px}
.topbar .signin{position:absolute;left:630px;top:7px;font-size:8px;color:var(--blue)}
.topbar .signup{position:absolute;left:662px;top:3px;width:52px;height:16px;background:var(--blue);color:#fff;font-size:8px;border-radius:2px;display:flex;align-items:center;justify-content:center}

/* header */
.header{position:absolute;top:24px;left:0;width:798px;height:59px;background:#fff;border-bottom:1px solid #e4e4e4}
.brand{position:absolute;left:83px;top:8px;display:flex;align-items:center;gap:6px;font-weight:700;color:var(--navy);line-height:1}
.brand .mark{width:12px;height:12px;background:var(--blue);border-radius:50%}
.brand .name{font-size:15px;line-height:17px}
.nav{position:absolute;left:265px;top:38px;display:flex;font-size:9px;color:var(--muted)}
.nav a{text-decoration:none;color:inherit;margin-right:25px}
.nav a:last-child{margin-right:0}
.nav a.active{color:var(--blue)}

/* hero */
.hero{position:absolute;top:83px;left:0;width:798px;height:263px;background:linear-gradient(90deg,#f4f4f4 0%,#ececec 45%,#f7f7f7 100%)}
.hero .copy{position:absolute;left:83px;top:62px;width:275px}
.hero .kicker{font-size:11.5px;font-weight:700;color:#444}
.hero h1{font-size:23px;font-weight:700;color:var(--blue);margin:3px 0 2px}
.hero .sub{font-size:11.5px;font-weight:700;color:#444;margin-bottom:8px}
.hero p{font-size:8.4px;line-height:15px;color:#555}
.hero .photo{position:absolute;left:397px;top:20px;width:320px;height:243px;background:radial-gradient(ellipse at 60% 45%,#d7d0ca 0%,#e6e3e0 45%,#f0f0f0 80%)}
.dots{position:absolute;left:377px;top:247px;display:flex;gap:3px}
.dots span{width:8px;height:8px;border-radius:50%;border:1px solid #aaa;background:#f4f4f4}
.dots span.on{background:#444}

/* features */
.features{position:absolute;top:346px;left:0;width:798px;height:199px;background:linear-gradient(100deg,var(--blue-deep) 0%,var(--blue-mid) 50%,var(--blue) 100%)}
.features .row{position:absolute;left:83px;top:22px;width:631px;display:flex;justify-content:space-between}
.feature{width:150px;text-align:center;color:#fff}
.feature .ring{width:70px;height:70px;margin:0 auto;border-radius:50%;background:var(--navy);border:5px solid #06325a;box-shadow:0 0 0 2px #0d4f86;display:flex;align-items:center;justify-content:center}
.feature .ring .inner{width:48px;height:48px;border-radius:50%;border:2px solid #fff;display:flex;align-items:center;justify-content:center}
.feature h3{font-size:11.5px;margin:11px 0 6px}
.feature p{font-size:7.4px;line-height:11px;color:#e3f0fa}
.feature .btn{display:inline-block;margin-top:10px;width:57px;height:17px;line-height:17px;background:var(--navy);color:#fff;font-size:7.4px;border-radius:2px}

/* pricing */
.pricing-title{position:absolute;top:558px;left:0;width:798px;text-align:center;font-size:18px;font-weight:700;color:#555}
.plans{position:absolute;top:599px;left:83px;width:631px;display:flex;justify-content:space-between}
.plan{width:154px;height:189px;border:1px solid #ccc;border-radius:0 0 3px 3px;background:linear-gradient(180deg,#fff 0%,#f4f4f4 60%,#ececec 100%);text-align:center}
.plan .head{height:44px;background:var(--navy);color:#fff;font-size:14px;font-weight:700;line-height:17px;padding-top:5px}
.plan .price{font-size:18px;font-weight:700;color:var(--blue);margin-top:12px}
.plan .incl{font-size:8px;font-weight:700;color:#222;margin-top:12px}
.plan .rate{font-size:11px;color:#555;margin-top:12px}
.plan .btn{display:inline-block;margin-top:12px;width:55px;height:16px;line-height:16px;background:var(--blue);color:#fff;font-size:7.4px;border-radius:2px}

/* testimonials */
.testimonials{position:absolute;top:815px;left:0;width:798px;height:216px;background:linear-gradient(180deg,#ececec,#e2e4e6);overflow:hidden}
.testimonials h2{position:relative;text-align:center;font-size:18px;color:var(--navy);margin-top:15px}
.testimonials .lead{position:relative;text-align:center;font-size:10.5px;color:#555;margin-top:8px}
.testimonials .ghost{position:absolute;left:105px;top:66px;font-size:78px;color:var(--ghost);letter-spacing:1px;white-space:nowrap}
.arrow{position:absolute;top:110px}
.quote{position:absolute;font-size:7.4px;line-height:12px;color:#666}
.quote .name{font-weight:700;color:var(--navy);font-size:8px}
.quote .place{color:var(--blue)}
.flag{display:inline-block;width:9px;height:6px;vertical-align:middle;margin:0 3px}
.q-left{left:114px;top:109px;width:200px;text-align:right}
.q-right{left:483px;top:84px;width:200px}
.avatar{position:absolute;border-radius:50%;border:3px solid #b7c2cb;background:radial-gradient(circle at 50% 40%,#9aa4ac,#5d6670)}
.av1{left:331px;top:110px;width:76px;height:76px}
.av2{left:389px;top:81px;width:76px;height:76px}

/* clients */
.clients{position:absolute;top:1030px;left:0;width:798px;height:137px;background:linear-gradient(90deg,#0d5e96,#1672b0 50%,#0e5e95)}
.clients h2{text-align:center;color:#fff;font-size:18px;margin-top:20px}
.clients .logos{position:absolute;left:108px;top:78px;width:580px;display:flex;justify-content:space-between;align-items:center}
.client{display:flex;align-items:center;gap:5px;font-size:14px;font-weight:700;color:#fff}
.client .dot{width:10px;height:10px;border-radius:50%;background:#fff}

/* footer */
.footer{position:absolute;top:1167px;left:0;width:798px;height:33px;background:var(--navy-dark)}
.footer .copy{position:absolute;left:83px;top:12px;font-size:7.4px;color:#fff}
.footer .copy span{color:var(--blue)}
.social{position:absolute;left:621px;top:7px;display:flex;gap:3px}
.social span{width:17px;height:17px;border-radius:50%;border:1px solid #fff}
</style>
</head>
<body>

<div class="topbar">
  <div class="call">
    <svg width="9" height="9" viewBox="0 0 24 24"><path fill="#1a8fd6" d="M6.6 10.8a15 15 0 0 0 6.6 6.6l2.2-2.2c.3-.3.7-.4 1-.2 1.1.4 2.3.6 3.6.6.6 0 1 .4 1 1V20c0 .6-.4 1-1 1A17 17 0 0 1 3 4c0-.6.4-1 1-1h3.5c.6 0 1 .4 1 1 0 1.3.2 2.5.6 3.6.1.3 0 .7-.2 1z"/></svg>
    Call us now : 1300 482 017
  </div>
  <div class="signin">Sign In</div>
  <div class="signup">Sign Up</div>
</div>

<header class="header">
  <div class="brand"><span class="mark"></span><span class="name">Velmarrow<br>Voice</span></div>
  <nav class="nav">
    <a class="active" href="#">Home</a>
    <a href="#">About</a>
    <a href="#">Products</a>
    <a href="#">Hosted PBX</a>
    <a href="#">Telephone Systems</a>
    <a href="#">Plans &amp; Signup</a>
    <a href="#">Contact Us</a>
  </nav>
</header>

<section class="hero">
  <div class="copy">
    <div class="kicker">Secure Internet Connection</div>
    <h1>Hosted PBX</h1>
    <div class="sub">Full Featured</div>
    <p>Hosted PBX is a cloud-based phone system entirely managed by Velmarrow Voice on a secure internet connection. You get a higher quality phone service and IP handsets loaded with even more features and abilities than standard phones and phone lines.</p>
  </div>
  <div class="photo" role="img" aria-label="Customer service agent with headset at a desk with laptop and desk phone"></div>
  <div class="dots"><span></span><span></span><span class="on"></span><span></span></div>
</section>

<section class="features">
  <div class="row">
    <div class="feature">
      <div class="ring"><div class="inner">
        <svg width="26" height="20" viewBox="0 0 26 20"><path d="M7 17h13a4.5 4.5 0 0 0 .5-9 6.5 6.5 0 0 0-12.5-1A5 5 0 0 0 7 17z" fill="none" stroke="#fff" stroke-width="1.6"/><rect x="10" y="8" width="6" height="7" rx="1" fill="none" stroke="#fff" stroke-width="1.2"/></svg>
      </div></div>
      <h3>Hosted PBX</h3>
      <p>Proin semper vulputate lorem, ac pretium eros pulvinar ut. Nunc malesuada venenatis, aliquam et enim.</p>
      <span class="btn">Read More</span>
    </div>
    <div class="feature">
      <div class="ring"><div class="inner">
        <svg width="24" height="24" viewBox="0 0 24 24"><path d="M4 14v-2a8 8 0 0 1 16 0v2" fill="none" stroke="#fff" stroke-width="1.8"/><rect x="3" y="13" width="4" height="6" rx="1.5" fill="#fff"/><rect x="17" y="13" width="4" height="6" rx="1.5" fill="#fff"/><path d="M19 19q0 3-6 3" fill="none" stroke="#fff" stroke-width="1.4"/></svg>
      </div></div>
      <h3>Brondavi Phones</h3>
      <p>Proin semper vulputate lorem, ac pretium eros pulvinar ut. Nunc malesuada venenatis, aliquam et enim.</p>
      <span class="btn">Read More</span>
    </div>
    <div class="feature">
      <div class="ring"><div class="inner">
        <svg width="24" height="24" viewBox="0 0 24 24"><rect x="6" y="6" width="12" height="12" rx="1" fill="#fff"/><g stroke="#fff" stroke-width="1.4"><path d="M9 2v4M12 2v4M15 2v4M9 18v4M12 18v4M15 18v4M2 9h4M2 12h4M2 15h4M18 9h4M18 12h4M18 15h4"/></g></svg>
      </div></div>
      <h3>ZelPBX</h3>
      <p>Proin semper vulputate lorem, ac pretium eros pulvinar ut. Nunc malesuada venenatis, aliquam et enim.</p>
      <span class="btn">Read More</span>
    </div>
    <div class="feature">
      <div class="ring"><div class="inner">
        <svg width="26" height="16" viewBox="0 0 26 16"><path d="M5 2h16l4 8v4H1v-4z" fill="#fff"/><rect x="1" y="10" width="24" height="1.2" fill="#0b2c4f"/><circle cx="20" cy="12.6" r="0.9" fill="#0b2c4f"/></svg>
      </div></div>
      <h3>Tusrok</h3>
      <p>Proin semper vulputate lorem, ac pretium eros pulvinar ut. Nunc malesuada venenatis, aliquam et enim.</p>
      <span class="btn">Read More</span>
    </div>
  </div>
</section>

<h2 class="pricing-title">VoIP Pricing Plans</h2>
<section class="plans">
  <div class="plan">
    <div class="head">Business<br>Starter</div>
    <div class="price">$0 month</div>
    <div class="incl">0 call included</div>
    <div class="rate">12c local calls</div>
    <div class="rate">24c mobile calls</div>
    <span class="btn">Sign Up Now</span>
  </div>
  <div class="plan">
    <div class="head">Business<br>Saver</div>
    <div class="price">$25 month</div>
    <div class="incl">250 local calls included</div>
    <div class="rate">10c local calls</div>
    <div class="rate">22c mobile</div>
    <span class="btn">Sign Up Now</span>
  </div>
  <div class="plan">
    <div class="head">Business<br>Super</div>
    <div class="price">$50 month</div>
    <div class="incl">500 local calls included</div>
    <div class="rate">09c local calls</div>
    <div class="rate">20c mobile calls</div>
    <span class="btn">Sign Up Now</span>
  </div>
  <div class="plan">
    <div class="head">Business<br>Extreme</div>
    <div class="price">$100 month</div>
    <div class="incl">1000 local calls included</div>
    <div class="rate">08c local calls</div>
    <div class="rate">18c mobile calls</div>
    <span class="btn">Sign Up Now</span>
  </div>
</section>

<section class="testimonials">
  <div class="ghost">“Testimonials</div>
  <h2>Clients Testimonials</h2>
  <div class="lead">What they say about our company</div>
  <svg class="arrow" style="left:89px" width="12" height="20" viewBox="0 0 12 20"><path d="M10 2 2 10l8 8" fill="none" stroke="#bbb" stroke-width="3"/></svg>
  <svg class="arrow" style="left:695px" width="12" height="20" viewBox="0 0 12 20"><path d="m2 2 8 8-8 8" fill="none" stroke="#bbb" stroke-width="3"/></svg>
  <div class="quote q-left">
    <div class="name">Tavin Rehlor</div>
    <div class="place">England<span class="flag" style="background:#c8102e"></span></div>
    Lorem ipsum dolor sit amet, consectetur adipiscing elit. Donec vestibulum eros vel lorem malesuada, at mollis mi volutpat. Nam in nunc fermentum, commodo odio quis, ullamcorper orci.
  </div>
  <div class="avatar av1" role="img" aria-label="Portrait photo of a smiling client in a suit"></div>
  <div class="avatar av2" role="img" aria-label="Portrait photo of a client on a phone call"></div>
  <div class="quote q-right">
    <div class="name">Orsen Valdique</div>
    <div class="place"><span class="flag" style="background:#74acdf;margin-left:0"></span>Argentina</div>
    Lorem ipsum dolor sit amet, consectetur adipiscing elit. Donec vestibulum eros vel lorem malesuada, at mollis mi volutpat. Nam in nunc fermentum, commodo odio quis, ullamcorper orci.
  </div>
</section>

<section class="clients">
  <h2>List Of Trusted Clients</h2>
  <div class="logos">
    <div class="client"><span class="dot"></span>quellith</div>
    <div class="client">lindavert</div>
    <div class="client"><span class="dot"></span>HarrowFinch</div>
    <div class="client">PelvanTools</div>
    <div class="client">ostrivo</div>
  </div>
</section>

<footer class="footer">
  <div class="copy">© Copyright 2012 <span>Velmarrow Voice</span>. All Rights Reserved</div>
  <div class="social"><span></span><span></span><span></span><span></span><span></span></div>
</footer>

</body>
</html>
```